Bright Reed Yellow Perch Fish Stock and immune system boosts

We are a non-profit that sets up Aquaponics's systems in cities of 5000 or less in the Midwest. We have created a product that uses our yellow perch carcasses as the base for this broth. Our fish are grown in containment from egg to market size fish. This means it is the safest most sustainable product on the market. We also use veggies grown in the same aquaponics system network. One product has oriental overtones and mixed with antioxidants as a gut immune system bacteria booster. The other is a standard broth that has multiple uses. We are looking for packaging for both our broths. We have included our logo (a pixel guild creation). This product packaging will also be a media piece promoting The Bright Reed way of life and a way to raise revenue for the non-profit. We have not chosen the names of products but will be under the "Bright Reed" verbiage. Example is " "Bright Reed Trout Tide stock"
I have added some current examples of packaging

Target Market(s)

consumers and commercial clients

Industry/Entity Type

Grocery Store

Colors

Designer to choose colors to be used in the design.

Requirements
Must have
• Fresh feeling, restorative qualities, safe, sustainable
• Package size is 32 oz. shape is flexible

```html
<!DOCTYPE html>
<html lang="en">
<head>
<meta charset="UTF-8">
<title>Bright Reed Cooking Stock – Carton Front</title>
<link rel="stylesheet" href="https://fonts.googleapis.com/css2?family=Open+Sans:wght@400;600&display=swap">
<style>
  :root {
    --backdrop: #e9e9e9;
    --green-deep: #24a43a;
    --green-mid: #5dbb35;
    --green-lime: #9ccb2c;
    --tab-white: #f7f7f5;
    --ink-blue: #1d4f8c;
    --ink-dark: #2b2b2b;
    --text-light: #ffffff;
    --pot-dark: #3a3a36;
    --pot-steam: #a7a79c;
  }
  * { box-sizing: border-box; margin: 0; padding: 0; }
  html, body {
    width: 1200px; height: 900px; overflow: hidden;
    background: var(--backdrop);
    font-family: "Open Sans", sans-serif;
  }
  .carton-front {
    position: absolute;
    left: 401px; top: 40px;
    width: 398px; height: 820px;
    background:
      radial-gradient(ellipse at 50% 62%, var(--green-lime) 0%, rgba(156,203,44,0) 60%),
      linear-gradient(180deg, var(--green-deep) 0%, var(--green-mid) 45%, var(--green-lime) 75%);
    overflow: hidden;
  }
  .brand-tab {
    position: absolute;
    left: 127px; top: 25px;
    width: 169px; height: 203px;
    background: var(--tab-white);
    border-radius: 0 0 8px 8px;
    display: flex; flex-direction: column; align-items: center;
    padding-top: 44px;
  }
  .brand-dot {
    width: 64px; height: 64px; border-radius: 50%;
    background: var(--ink-blue);
    margin-bottom: 26px;
  }
  .brand-name {
    font-size: 22px; font-weight: 400; color: var(--ink-dark);
    letter-spacing: 0.5px; line-height: 1;
  }
  .brand-region {
    margin-top: 5px;
    font-size: 11.5px; color: var(--ink-dark); letter-spacing: 0.3px;
  }
  .product-title {
    position: absolute; left: 0; right: 0; top: 320px;
    text-align: center; color: var(--text-light);
    font-size: 42px; line-height: 40px; font-weight: 400;
  }
  .product-variant {
    position: absolute; left: 50%; top: 410px;
    transform: translateX(-50%);
    padding: 0 14px;
    background: rgba(255,255,255,0.12);
    border-radius: 16px;
    color: var(--text-light); font-size: 31px; line-height: 38px;
  }
  .product-claim {
    position: absolute; left: 0; right: 0; top: 455px;
    text-align: center; color: var(--text-light);
    font-size: 19px; word-spacing: 6px;
  }
  .serving-photo {
    position: absolute; left: 0; right: 0; top: 490px; bottom: 0;
    border-radius: 55% 55% 0 0 / 28px 28px 0 0;
    background:
      radial-gradient(ellipse at 60% 55%, #c9c7b0 0%, rgba(201,199,176,0) 55%),
      linear-gradient(160deg, var(--pot-steam) 0%, var(--pot-dark) 100%);
  }
  .nutrition-facts {
    position: absolute; left: 2px; bottom: 6px;
    display: flex; gap: 2px;
  }
  .fact {
    width: 33px; height: 57px;
    background: var(--ink-blue);
    border: 1px solid #e6eef7; border-radius: 3px;
    color: var(--text-light); text-align: center;
    display: flex; flex-direction: column; justify-content: center;
  }
  .fact.wide { width: 35px; }
  .fact-value { font-size: 22px; line-height: 26px; }
  .fact.wide .fact-value { font-size: 12px; line-height: 26px; }
  .fact-label { font-size: 7px; line-height: 12px; }
  .net-weight {
    position: absolute; right: 4px; bottom: 6px;
    background: var(--ink-blue); color: var(--text-light);
    border: 1px solid #e6eef7; border-radius: 3px;
    font-size: 8px; padding: 1px 4px;
  }
</style>
</head>
<body>
  <main class="carton-front">
    <section class="brand-tab">
      <div class="brand-dot"></div>
      <div class="brand-name">BRIGHT REED</div>
      <div class="brand-region">GREAT LAKES REGION</div>
    </section>

    <h1 class="product-title">COOKING<br>STOCK</h1>
    <div class="product-variant">VEGGIES</div>
    <div class="product-claim">100% NATURAL</div>

    <div class="serving-photo" role="img" aria-label="Steaming hot pot with fish, shiitake mushrooms, carrot flowers, cabbage and leeks"></div>

    <div class="nutrition-facts">
      <div class="fact"><span class="fact-value">15</span><span class="fact-label">Calories</span></div>
      <div class="fact"><span class="fact-value">0</span><span class="fact-label">Salt Fat</span></div>
      <div class="fact wide"><span class="fact-value">550g</span><span class="fact-label">Sodium</span></div>
      <div class="fact"><span class="fact-value">2</span><span class="fact-label">Sugar</span></div>
    </div>
    <div class="net-weight">NET WT: 32 Oz (213) (907G)</div>
  </main>
</body>
</html>
```